Website for a company offering full serivce charging solutions for electric cars

The company "mero-kant" (english: "mero-edge") offering all-in-one-solutions for charging infrastructure for electric mobility.

There are four products:
1- Wallboxes for single-family homes
2- Solutions for property devloper/-management for property parking space
3- All-in-one-charging solution for municipalities/communities
4- Solutions for tourism/hotels/holiday appartments

The Website structure:
1. Main Page
2.1. Product Page Single Homes
2.2. Product Page Property Management / Parking
2.3. Product Page Municipality
2.4. Product Page Tourism
3. Contact Form / Request for information
4. Imprint / Legal

The Website should be built on Wordpress with a powerful possibility to simply add/modify specific landing pages.

We would like you to implement the website later and also maintain it if possible, but we would be able to do minor modifications by ourselfs (for A/B-Testing)

The website should be clear and simple, easy to understand.
Target group is mainly B2C without deeper knowledge of that topic.

It should suggest, that we will provide a very simple way to get the charging infrastructure done.

We need a contact form, maybe we will use Hubspot later.

Attached you will find a draft of the main page and a landing page (for 2.2) - it is just the content, please ignore the design. We would love to let you create a suitable design.
Also you will find some drafts a bit different for the same story.

I added also a few stock photos, but they don't need to be used! If you have better ideas, you are welcome!

Industry/Entity Type

Charging/Electric mobility

Number of Pages Required

2 page

Font styles to use
Sans Serif

Requirements
Must have
• Based on Wordpress, and the designer should be able to implement it on Wordpress on a later step

```html
<!DOCTYPE html>
<html lang="de">
<head>
<meta charset="utf-8">
<title>mero-kant.de – Ladelösungen</title>
<link href="https://fonts.googleapis.com/css2?family=Orbitron:wght@600;700&family=Montserrat:wght@400;500;600&display=swap" rel="stylesheet">
<style>
:root{
  --pink:#e0169e;
  --violet:#8a55c6;
  --grad:linear-gradient(90deg,var(--pink),var(--violet));
  --navy:#101828;
  --black:#000;
  --white:#fff;
  --ink:#111;
  --hero-a:#5b6474;
  --hero-b:#9aa2b0;
}
*{box-sizing:border-box;margin:0;padding:0}
html,body{width:1200px;height:2297px;overflow:hidden}
body{font-family:"Montserrat",sans-serif;color:var(--ink);background:var(--white);position:relative}
.display{font-family:"Orbitron",sans-serif;font-weight:700;text-transform:uppercase;letter-spacing:.5px}
.btn{display:inline-flex;align-items:center;justify-content:center;border-radius:22px;background:var(--grad);color:var(--white);font-family:"Orbitron",sans-serif;font-weight:600;font-size:15px;text-transform:uppercase;text-decoration:none}
.brand{font-family:"Montserrat",sans-serif;font-weight:500;color:var(--white);display:flex;align-items:center;gap:10px}
.brand-dot{width:12px;height:12px;border-radius:50%;background:var(--pink)}

/* hero */
.hero{position:absolute;left:0;top:0;width:1200px;height:686px;background:linear-gradient(115deg,#48505f 0%,var(--hero-a) 30%,var(--hero-b) 70%,#b7bdc8 100%)}
.hero-photo{position:absolute;inset:0;background:radial-gradient(circle at 38% 42%,rgba(190,120,150,.35),transparent 35%),radial-gradient(circle at 62% 25%,rgba(40,46,60,.45),transparent 30%)}
.site-header .brand{position:absolute;left:110px;top:84px;font-size:31px}
.contact{position:absolute;top:26px;display:flex;align-items:center;gap:14px;color:var(--white);font-size:14px}
.contact-icon{width:36px;height:36px;border:1.5px solid var(--white);border-radius:50%;display:flex;align-items:center;justify-content:center}
.contact.mail{left:720px}
.contact.phone{left:923px;font-size:13px}
.main-nav{position:absolute;left:420px;top:90px;display:flex;gap:29px;font-size:15.5px;color:var(--white)}
.login{position:absolute;left:940px;top:82px;width:150px;height:39px;font-size:15px}
.hero-copy{position:absolute;left:0;right:0;top:310px;text-align:center;color:var(--white)}
.hero-copy h1{font-size:40px;font-weight:600;letter-spacing:1px}
.hero-copy p{width:740px;margin:22px auto 0;font-size:16px;line-height:27px}
.hero-copy .btn{margin-top:22px;width:171px;height:39px}
.dots{position:absolute;top:608px;left:561px;display:flex;gap:9px}
.dots span{width:13px;height:13px;border-radius:50%;background:var(--white)}
.dots span.active{background:transparent;border:2px solid var(--pink)}

/* partner */
.partner{position:absolute;top:686px;left:0;width:1200px;height:507px}
.partner h2{position:absolute;left:126px;top:90px;font-size:31px;line-height:40px;width:420px}
.partner p{position:absolute;left:129px;top:176px;width:515px;font-size:16px;line-height:26px;text-align:justify}
.partner .btn{position:absolute;left:129px;top:377px;width:223px;height:39px}
.partner-photo{position:absolute;left:728px;top:90px;width:345px;height:335px;border-radius:50%;background:radial-gradient(circle at 70% 50%,#2f5ef0 0%,#8aa4f4 30%,#e6e6ea 55%,#cfd0d4 100%);border-right:5px solid var(--violet)}

/* solutions */
.solutions{position:absolute;top:1193px;left:0;width:1200px;height:785px;background:var(--navy);color:var(--white)}
.solutions h2{position:absolute;left:0;right:0;top:80px;text-align:center;font-size:30px;line-height:37px}
.card{position:absolute;top:232px;height:430px;border-radius:6px;padding:38px 36px 0}
.card.outline{border:3px solid transparent;background:linear-gradient(var(--navy),var(--navy)) padding-box,var(--grad) border-box}
.card.filled{background:var(--grad)}
.card h3{font-family:"Orbitron",sans-serif;font-weight:600;font-size:17px;text-transform:uppercase;margin-bottom:20px}
.card.outline h3{background:var(--grad);-webkit-background-clip:text;background-clip:text;color:transparent}
.card ul{list-style:none}
.card li{display:flex;align-items:center;gap:12px;font-size:12px;font-weight:600;line-height:18px;height:54px;margin-bottom:10px}
.card li::before{content:"»";font-size:15px;flex:none}
.card .btn{position:absolute;left:36px;bottom:44px;width:223px;height:39px}
.card.filled .btn{background:transparent;border:2px solid var(--white)}
.c1{left:109px;width:317px}
.c2{left:444px;width:312px}
.c3{left:773px;width:317px}

/* footer */
.site-footer{position:absolute;top:1978px;left:0;width:1200px;height:319px;background:var(--black);color:var(--white)}
.site-footer .brand{position:absolute;left:0;right:0;top:70px;justify-content:center;font-size:27px}
.footer-nav{position:absolute;left:0;right:0;top:150px;display:flex;justify-content:center;gap:26px;font-size:16px}
.social{position:absolute;left:519px;top:178px;display:flex;gap:16px}
.social span{width:28px;height:28px;border-radius:50%;background:var(--grad)}
.rule{position:absolute;left:85px;top:240px;width:977px;height:1px;background:#555}
.copyright{position:absolute;left:0;right:0;top:272px;text-align:center;font-size:12px}
</style>
</head>
<body>

<section class="hero">
  <div class="hero-photo" role="img" aria-label="Ladestecker steckt in der Ladebuchse eines Elektroautos"></div>
  <header class="site-header">
    <div class="brand"><span class="brand-dot"></span>mero-kant.de</div>
    <div class="contact mail">
      <span class="contact-icon"><svg width="16" height="12" viewBox="0 0 16 12"><rect x="0.5" y="0.5" width="15" height="11" rx="1.5" fill="#fff"/><path d="M1 1l7 6 7-6" stroke="#5b6474" stroke-width="1.4" fill="none"/></svg></span>
      info@merokant.in
    </div>
    <div class="contact phone">
      <span class="contact-icon"><svg width="15" height="15" viewBox="0 0 24 24"><path fill="#fff" d="M6.6 10.8a15 15 0 006.6 6.6l2.2-2.2a1 1 0 011-.25 11.4 11.4 0 003.6.57 1 1 0 011 1V20a1 1 0 01-1 1A17 17 0 013 4a1 1 0 011-1h3.5a1 1 0 011 1c0 1.25.2 2.45.57 3.57a1 1 0 01-.25 1z"/></svg></span>
      +1 555 010 0199
    </div>
    <nav class="main-nav"><span>Losungen</span><span>Unternehmen</span><span>Services</span><span>Karriere</span><span>Kontakt</span></nav>
    <a class="btn login">Einloggen</a>
  </header>
  <div class="hero-copy">
    <h1 class="display">Willkommen zu Mero Kant DE</h1>
    <p>Lorem ipsum dolor sit amet, consectetur adipiscing elit, sed do eiusmod tempor incididunt ut labore et dolore magna aliqua. Ut enim ad minim veniam</p>
    <a class="btn">Loslegen</a>
  </div>
  <div class="dots"><span class="active"></span><span></span><span></span><span></span></div>
</section>

<section class="partner">
  <h2 class="display">Mero-kant ist Ihr Partner</h2>
  <p>wenn das Laden nicht nur einfach, sondern die Umsetzung auch aus einer Hand kommen soll Wir  bieten Lösungen sowohl für Privatkunden, Geschäftskunden als auch Kommunen an, die schnell, fair und ohne Eigenleistung zu einer smarten Ladelösung für E-Fahrzeuge kommen möchten.Von der Beratung, über die Installation, Inbetriebnahme bis zur Abrechnung und Wartung bekommen Sie bei mero-kant alles aus einer Hand. Auf Wunsch</p>
  <a class="btn">Erfahren Sie mehr</a>
  <div class="partner-photo" role="img" aria-label="Weißer Ladestecker in blau beleuchteter Ladebuchse"></div>
</section>

<section class="solutions">
  <h2 class="display">Fragen Sie uns nach der auf Ihre<br>individuellen Bedürfnisse zugeschnittenen<br>Lösung:</h2>

  <article class="card outline c1">
    <h3>Als Privatkunde</h3>
    <ul>
      <li>Bestandsanalyse mitumfangreicher Beratung über die Möglichkeiten der Umsetzung</li>
      <li>Prüfung und Übernahme der Anmeldung verfügbarer Fördermöglichkeiten</li>
      <li>Auswahl an smarten Wallbox Lösungen, passend für Ihr Fahrzeug und Ihre Bedürfnisse</li>
      <li>Installation inkl. aller notwendigen Materialien und Tätigkeiten (Durchbrüche, Erdarbeiten, etc.)</li>
    </ul>
    <a class="btn">Erfahren Sie mehr</a>
  </article>

  <article class="card filled c2">
    <h3>Als Geschäftskunde</h3>
    <ul>
      <li>Durchführung einer individuellen Bedarfsanalyse inkl. Ermittlung der Anforderungen für</li>
      <li>Planung und Projektierung des Installationsaufwands inkl. Materialverbrauch</li>
      <li>Normgerechte Installation der Ladeinfrastruktur inkl. Durchbruch-, Brandschutz- und</li>
      <li>Inbetriebnahme der Anlage inkl. Prüf- und Messprotokollen</li>
    </ul>
    <a class="btn">Erfahren Sie mehr</a>
  </article>

  <article class="card outline c3">
    <h3>Als Kommune</h3>
    <ul>
      <li>Konzeptionierung möglicher Ladeinfrastrukturen innerhalb Ihrer Gemeinde</li>
      <li>Planung und Projektsteuerung inkl. sämtlicher behördlicher Genehmigungsverfahren und</li>
      <li>Fachgerechte Installation und Inbetriebnahme</li>
      <li>Regelmäßige Wartung gemäß Vorschrif</li>
    </ul>
    <a class="btn">Erfahren Sie mehr</a>
  </article>
</section>

<footer class="site-footer">
  <div class="brand"><span class="brand-dot"></span>mero-kant.de</div>
  <nav class="footer-nav"><span>Losungen</span><span>I</span><span>Unternehmen</span><span>I</span><span>Services</span><span>I</span><span>Karriere</span><span>I</span><span>Kontakt</span></nav>
  <div class="social"><span></span><span></span><span></span><span></span></div>
  <div class="rule"></div>
  <p class="copyright">Copyrights © 2022 mero-kant All rights reserved.</p>
</footer>

</body>
</html>
```